Maple Ridge business card design

Card needs to include the following text/items:
Company Logo
Rupert Hollis
Phone # - 517-386-9042
service@mapleridgelandscaping.example
Lawn & landscape maintenance services

```html
<!DOCTYPE html>
<html lang="en">
<head>
<meta charset="utf-8">
<title>Maple Ridge Landscaping – Business Card</title>
<link href="https://fonts.googleapis.com/css2?family=Cinzel:wght@700&family=Montserrat:wght@400;500&display=swap" rel="stylesheet">
<style>
  :root {
    --bg: #e9ecec;
    --card: #ffffff;
    --forest: #1f4d2b;
    --olive: #7a9a3c;
    --sky: #1bc2f0;
    --orange: #f5a623;
    --ink: #1c1c1c;
  }
  * { margin: 0; padding: 0; box-sizing: border-box; }
  html, body { width: 1200px; height: 960px; overflow: hidden; }
  body {
    background: var(--bg);
    font-family: "Montserrat", sans-serif;
    display: flex;
    flex-direction: column;
    align-items: center;
    justify-content: center;
    gap: 40px;
  }
  .card {
    position: relative;
    width: 720px;
    height: 411px;
    background: var(--card);
    box-shadow: 0 6px 22px rgba(0,0,0,.18);
    overflow: hidden;
  }
  .brand {
    display: flex;
    flex-direction: column;
    align-items: center;
  }
  .brand-mark {
    border-radius: 50%;
    background: linear-gradient(180deg, #8fd3f2 0%, #3f7a3a 60%, #24502a 100%);
    border: 3px solid var(--olive);
  }
  .brand-name {
    font-family: "Cinzel", serif;
    font-weight: 700;
    color: var(--forest);
    text-align: center;
    line-height: 1.1;
  }
  /* Front */
  .card-front .brand { position: absolute; inset: 0; justify-content: center; gap: 18px; }
  .card-front .brand-mark { width: 170px; height: 170px; }
  .card-front .brand-name { font-size: 40px; }
  /* Back */
  .card-back .brand { position: absolute; top: 26px; left: 0; right: 0; gap: 8px; }
  .card-back .brand-mark { width: 86px; height: 86px; }
  .card-back .brand-name { font-size: 22px; }
  .holder {
    position: absolute; top: 168px; left: 0; right: 0;
    text-align: center;
    font-family: "Cinzel", serif; font-weight: 700; font-size: 30px;
    letter-spacing: 1px;
  }
  .holder .first { color: var(--orange); }
  .holder .last { color: var(--sky); }
  .tagline {
    position: absolute; top: 214px; left: 0; right: 0;
    text-align: center; font-size: 15px; color: var(--ink);
  }
  .contacts {
    position: absolute; top: 244px; left: 0; right: 0;
    display: flex; justify-content: center; gap: 22px;
    font-size: 15px; color: var(--ink);
  }
  .contact { display: flex; align-items: center; gap: 7px; }
  .contact svg { width: 16px; height: 16px; flex: none; }
  .website {
    position: absolute; top: 274px; left: 0; right: 0;
    display: flex; justify-content: center;
    font-size: 15px; color: var(--ink);
  }
  .wave { position: absolute; left: 0; bottom: 0; width: 720px; height: 150px; }
</style>
</head>
<body>

  <section class="card card-front">
    <div class="brand">
      <div class="brand-mark" role="img" aria-label="Round landscape emblem with trees, fence and setting sun"></div>
      <div class="brand-name">Maple Ridge Landscaping</div>
    </div>
  </section>

  <section class="card card-back">
    <div class="brand">
      <div class="brand-mark" role="img" aria-label="Round landscape emblem with trees, fence and setting sun"></div>
      <div class="brand-name">Maple Ridge Landscaping</div>
    </div>

    <div class="holder"><span class="first">Rupert</span> <span class="last">Hollis</span></div>
    <p class="tagline">Lawn &amp; landscape maintenance services</p>

    <div class="contacts">
      <span class="contact">
        <svg viewBox="0 0 24 24" aria-hidden="true"><path fill="#1bc2f0" d="M6.6 10.8a15.1 15.1 0 0 0 6.6 6.6l2.2-2.2a1 1 0 0 1 1-.25 11.4 11.4 0 0 0 3.6.57 1 1 0 0 1 1 1V20a1 1 0 0 1-1 1A17 17 0 0 1 3 4a1 1 0 0 1 1-1h3.5a1 1 0 0 1 1 1c0 1.25.2 2.45.57 3.57a1 1 0 0 1-.25 1z"/></svg>
        517-386-9042
      </span>
      <span class="contact">
        <svg viewBox="0 0 24 24" aria-hidden="true"><path fill="#1bc2f0" d="M2 5h20v14H2z"/><path fill="none" stroke="#fff" stroke-width="1.6" d="M2 5l10 8 10-8"/></svg>
        service@mapleridgelandscaping.example
      </span>
    </div>

    <div class="website">
      <span class="contact">
        <svg viewBox="0 0 24 24" aria-hidden="true"><circle cx="12" cy="12" r="10" fill="#1bc2f0"/><path fill="none" stroke="#fff" stroke-width="1.3" d="M2 12h20M12 2c3 3 3 17 0 20M12 2c-3 3-3 17 0 20"/></svg>
        www.mapleridgelandscaping.example
      </span>
    </div>

    <svg class="wave" viewBox="0 0 720 150" preserveAspectRatio="none" aria-hidden="true">
      <path d="M0 150 L0 118 C240 120 470 80 720 0 L720 150 Z" fill="var(--sky)"/>
      <path d="M220 118 C420 100 560 50 720 -8" fill="none" stroke="var(--card)" stroke-width="8"/>
      <path d="M240 112 C430 92 570 40 720 -14" fill="none" stroke="var(--forest)" stroke-width="4"/>
    </svg>
  </section>

</body>
</html>
```